Web site design for Brivolt Software (www.brivoltsoftware-example.com)

Need the design as well as the html for the website. The brief is given in the attached file.
If possible, would like to use pencil sketches instead of images to give a unique look to the site.
Target Market(s)
small Software product companies
Industry/Entity Type
Software
Coding
Coded - Design and coding required
Number of Pages Required
5+ page

```html
<!DOCTYPE html>
<html lang="en">
<head>
<meta charset="utf-8">
<title>Brivolt Software — Services</title>
<link href="https://fonts.googleapis.com/css2?family=Courier+Prime:wght@400;700&display=swap" rel="stylesheet">
<style>
:root{
  --bg:#26272b;
  --panel:#1b1b1e;
  --rule:#4a4b50;
  --text:#ffffff;
  --muted:#8d8e93;
  --accent:#2ee6e6;
}
*{margin:0;padding:0;box-sizing:border-box}
html,body{width:711px;height:1200px;overflow:hidden;background:var(--bg)}
body{position:relative;font-family:"Courier Prime","Courier New",monospace;color:var(--text)}
.abs{position:absolute}
.column-rule{position:absolute;top:0;width:1px;height:1200px;background:var(--rule)}
.menu-panel{left:86px;top:0;width:179px;height:401px;background:var(--panel)}
.sketch{left:86px;top:40px;width:440px;height:330px;
  background:radial-gradient(ellipse at 35% 45%,rgba(120,120,125,.22),rgba(38,39,43,0) 60%),
             radial-gradient(ellipse at 80% 45%,rgba(120,120,125,.16),rgba(38,39,43,0) 55%)}
.brand-name{left:94px;top:11px;font-size:12px;font-weight:400;letter-spacing:.5px}
.page-title{left:272px;top:11px;font-size:12px;letter-spacing:.5px}
.cta{left:533px;top:9px;width:83px;height:19px;border:1.5px solid #fff;border-radius:10px;
  font-size:6px;font-weight:700;display:flex;align-items:center;justify-content:center;gap:5px}
.site-nav{left:37px;top:0}
.site-nav a{position:absolute;left:0;white-space:nowrap;font-size:3.8px;color:var(--muted);text-decoration:none;letter-spacing:.3px}
.site-nav a.current{font-size:8px;color:var(--accent);letter-spacing:.5px}
.service-menu{left:101px;top:0}
.service-menu span{position:absolute;left:0;font-size:5px;color:#cfcfd2;width:70px;line-height:6px;white-space:nowrap}
.quote-author{left:272px;top:90px;font-size:14px;letter-spacing:1px}
.quote-line{left:272px;font-size:7px;letter-spacing:.2px}
.scroll-hint{left:632px;top:390px;font-size:5px}
.service{font-size:5.3px;line-height:7.4px}
.service h2{font-size:5.3px;font-weight:700;letter-spacing:.2px}
.illustration{border-radius:4px}
</style>
</head>
<body>
  <div class="abs menu-panel"></div>
  <div class="abs sketch" role="img" aria-label="Faint pencil sketch portrait of a bearded philosopher"></div>

  <div class="column-rule" style="left:86px"></div>
  <div class="column-rule" style="left:265px"></div>
  <div class="column-rule" style="left:444px"></div>
  <div class="column-rule" style="left:624px"></div>

  <div class="abs brand-name">Brivolt Software</div>
  <div class="abs page-title">_Services</div>
  <div class="abs cta">WORK WITH US <svg width="7" height="5" viewBox="0 0 7 5"><path d="M0 2.5h6M4 .5l2 2-2 2" stroke="#fff" fill="none" stroke-width=".8"/></svg></div>

  <nav class="abs site-nav">
    <a style="top:67px">HOME</a>
    <a class="current" style="top:89px">SERVICES</a>
    <a style="top:117px">ABOUT US</a>
    <a style="top:140px">EXPERTISE</a>
    <a style="top:165px">ENGAGEMENT MODELS</a>
    <a style="top:190px">AGILE</a>
    <a style="top:214px">CASE STUDIES</a>
    <a style="top:238px">ACCOLADES</a>
    <a style="top:262px">STORIES</a>
    <a style="top:287px">PARTNERS</a>
    <a style="top:312px">MYTHS MADE</a>
    <a style="top:335px">BLOG</a>
    <a style="top:360px">CONTACT US</a>
  </nav>

  <div class="abs service-menu">
    <span style="top:78px">POC</span>
    <span style="top:102px">Build product</span>
    <span style="top:127px">Maintain product</span>
    <span style="top:153px">ODC setup</span>
    <span style="top:177px">Architectural<br>interventions</span>
    <span style="top:208px">Agile Consulting</span>
    <span style="top:232px">SMEs</span>
    <span style="top:257px">High end Training</span>
    <span style="top:282px">Custom Development</span>
    <span style="top:306px">Predictive<br>Analytics</span>
  </div>

  <div class="abs quote-author">Aldric Venn</div>
  <div class="abs quote-line" style="top:136px">We are what we repeatedly do.</div>
  <div class="abs quote-line" style="top:155px">Excellence, then, is not an act,</div>
  <div class="abs quote-line" style="top:173px">but a habit.</div>
  <div class="abs scroll-hint">Scroll down_</div>

  <section class="abs service" style="left:102px;top:436px;width:153px">
    <h2>POC</h2>
    <p>Whether it is a mobile or web app prototype, or a more complex IoT prototype, our engineers can understand the requirements, the context, the technology stack and quickly collaborate with you to build a POC showing the proposed capabilities of a product.<br>Some of the POCs built by us include a system for quickly finding lawyers based on expertise, location etc; a system using IoT to track cashvans; and an app for doctors to reverse chronic diseases in patients using a regimen backed by gamification.</p>
  </section>
  <div class="abs illustration" style="left:350px;top:425px;width:189px;height:118px;background:linear-gradient(135deg,#3a3c42,#d8dde2 55%,#f5c9c3)" role="img" aria-label="Illustration of responsive devices with HTML, Java and CSS tags"></div>

  <section class="abs service" style="left:460px;top:593px;width:152px">
    <h2>BUILD PRODUCT</h2>
    <p>Our team of analysts, design thinkers and technologists work with client and end users to specify and carve out a product; our technologists architect and design the product; and UI designers work with engineers to deliver what is required in a timely manner.<br>Agile processes are followed - we use user stories, backlogs, TDD, CI, and practices such as standup meetings and pair programming to deliver software Just In time with adequate quality.<br>Product life cycles are usually long, going up to decades. Our clients have stayed with us for long periods.</p>
  </section>
  <div class="abs illustration" style="left:173px;top:603px;width:185px;height:105px;background:linear-gradient(160deg,#2c2f38,#5a6270 60%,#e9ecef)" role="img" aria-label="Illustration of laptop, tablet and phone showing a website"></div>

  <section class="abs service" style="left:98px;top:759px;width:156px">
    <h2>MAINTAIN PRODUCT</h2>
    <p>We have the ability to quickly understand large, legacy products, write scaffold test cases around them, and then maintain them with minimum team size and minimum fuss.<br>Our technical knowledge in languages such as C,C++,Java, .NET, LAMP stack, and Nodejs, as well as in depth understanding of data formats, data transmission, networking on different protocol levels, and middleware, helps us in mastering practically any product and providing timely and adequate support.<br>Expertise extends beyond technical knowledge to processes, customer orientation, service mindedness, and well defined processes, which are sometimes transcended to help customers, but never bypassed.</p>
  </section>
  <div class="abs illustration" style="left:342px;top:770px;width:208px;height:109px;background:linear-gradient(135deg,#2b2d33,#3f434b 60%,#23252a)" role="img" aria-label="Illustration of a developer desk with code screen and language tags"></div>

  <div class="abs illustration" style="left:160px;top:928px;width:212px;height:117px;background:linear-gradient(135deg,#f3f3f3,#2a7be8 45%,#f2786c)" role="img" aria-label="Illustration of wireframes, blueprint and design tools"></div>
  <section class="abs service" style="left:459px;top:966px;width:155px">
    <h2>ODC SETUP</h2>
    <p>We help in setting up Offshore Development centres for small and medium software development companies in Europe and US. More on "Models" section.</p>
  </section>

  <section class="abs service" style="left:98px;top:1086px;width:156px">
    <h2>ARCHITECTURAL INTERVENTIONS</h2>
    <p>Does your product refuse to scale? Is it bogged down by unpredictable, unreplicable issues brought out by concurrency? Are there regressions every time some feature is added? Or is expertise required in some particular technology?<br><br>We can help. We bring our expertise in large scale software development to analyse the architecture, and suggest minimal interventions to get it back on track.</p>
  </section>
  <div class="abs illustration" style="left:383px;top:1082px;width:123px;height:93px;background:linear-gradient(135deg,#29b8e0,#f06f7f 45%,#1ee8b8 70%,#f4b32a)" role="img" aria-label="Illustration of connected files over a browser window"></div>
</body>
</html>
```